Lionel Marsbeck Card

My father, Lionel Marsbeck, just retired at 69 years old and he needs a new business/social card that looks professional and includes some sort of logo - perhaps his initials LM. It needs to include his phone number and email address and that's it. So fairly limited text but still elegant.

Industry/Entity Type

Business

```html
<!DOCTYPE html>
<html lang="en">
<head>
<meta charset="utf-8">
<title>Lionel Marsbeck – Business Card</title>
<link rel="stylesheet" href="https://fonts.googleapis.com/css2?family=Exo+2:ital,wght@0,700;1,700&family=Open+Sans:wght@400;600&display=swap">
<style>
  :root {
    --card-light: #f4f4f4;
    --card-mid: #e2e2e2;
    --band-dark: #2e2e2e;
    --band-mid: #585858;
    --accent-blue: #4fa6e3;
    --name-ink: #3a3a3a;
    --monogram-ink: #6b6b6b;
    --contact-ink: #ffffff;
  }
  * { margin: 0; padding: 0; box-sizing: border-box; }
  html, body {
    width: 1200px;
    height: 750px;
    overflow: hidden;
    background: #ffffff;
  }
  .card {
    position: relative;
    width: 1200px;
    height: 750px;
    background: radial-gradient(ellipse at 70% 45%, var(--card-light) 0%, var(--card-mid) 100%);
    overflow: hidden;
    font-family: "Open Sans", Arial, sans-serif;
  }
  .card-shapes {
    position: absolute;
    inset: 0;
  }
  .monogram {
    position: absolute;
    left: 600px;
    top: 150px;
    width: 520px;
    text-align: center;
    font-family: "Exo 2", Arial, sans-serif;
    font-weight: 700;
    font-size: 270px;
    line-height: 1;
    color: var(--monogram-ink);
    letter-spacing: -6px;
  }
  .identity-name {
    position: absolute;
    left: 41px;
    top: 462px;
    font-family: "Exo 2", Arial, sans-serif;
    font-style: italic;
    font-weight: 700;
    font-size: 44px;
    line-height: 1.2;
    color: var(--name-ink);
    text-transform: uppercase;
    letter-spacing: 0.5px;
  }
  .contact {
    position: absolute;
    display: flex;
    align-items: center;
    gap: 12px;
    color: var(--contact-ink);
    font-size: 25px;
    letter-spacing: 0.3px;
  }
  .contact svg { width: 26px; height: 26px; flex: none; }
  .contact-desk { left: 46px; top: 555px; }
  .contact-mobile { left: 46px; top: 658px; }
  .contact-mail { left: 306px; top: 658px; }
</style>
</head>
<body>
<main class="card">
  <svg class="card-shapes" width="1200" height="750" viewBox="0 0 1200 750" aria-hidden="true">
    <defs>
      <linearGradient id="bandGradient" x1="0" y1="0" x2="1" y2="1">
        <stop offset="0" stop-color="var(--band-dark)"/>
        <stop offset="1" stop-color="var(--band-mid)"/>
      </linearGradient>
    </defs>
    <path d="M618 0 C630 4 638 12 646 26 C656 44 666 62 694 62 L1200 62" fill="none" stroke="var(--accent-blue)" stroke-width="4"/>
    <path d="M626 0 L1200 0 L1200 56 L700 56 C676 56 666 40 656 24 C648 12 640 4 626 0 Z" fill="url(#bandGradient)"/>
    <path d="M0 524 H565 C605 524 615 552 635 582 C655 612 670 626 705 626 H1200" fill="none" stroke="var(--accent-blue)" stroke-width="4"/>
    <path d="M0 532 H560 C598 532 608 560 628 590 C648 620 664 634 700 634 H1200 V750 H0 Z" fill="url(#bandGradient)"/>
  </svg>

  <div class="monogram">LM</div>

  <h1 class="identity-name">Lionel Marsbeck</h1>

  <div class="contact contact-desk">
    <svg viewBox="0 0 24 24" fill="var(--accent-blue)"><rect x="3" y="3" width="6" height="18" rx="1.5"/><rect x="10" y="7" width="11" height="14" rx="1.5"/><rect x="12" y="9" width="7" height="3" fill="#2e2e2e"/></svg>
    <span>744 21 58 63 07</span>
  </div>
  <div class="contact contact-mobile">
    <svg viewBox="0 0 24 24"><rect x="6" y="2" width="12" height="20" rx="2" fill="var(--accent-blue)"/><rect x="8" y="5" width="8" height="12" fill="#2e2e2e"/><circle cx="12" cy="19.5" r="1" fill="#2e2e2e"/></svg>
    <span>748 90 16 27 33</span>
  </div>
  <div class="contact contact-mail">
    <svg viewBox="0 0 24 24"><rect x="3" y="6" width="18" height="12" rx="1" fill="var(--accent-blue)"/><path d="M3 6 L12 13 L21 6" fill="none" stroke="#2e2e2e" stroke-width="1.5"/></svg>
    <span>lionel@marsbeck.net</span>
  </div>
</main>
</body>
</html>
```